Business Card Update, need to bring life to the card, two sided color

We need a new business card design, are moving and changing addresses and need a new look, we have the logos already attached but need a new style moving forward. Can incorporate the color of the logo (The Green) as well, maybe a solid back? We deal with safety products revolving around static electricity and safety lighting. Would like to keep same font in second logo as well.

Target Market(s)

Electrical Safety, Lighting

Contact Information for Business Card

Marco Tillet
Vice President
Office: 555-284-7130
Cell: 555-619-3842
marco@kvtillet.example
www.kvtillet.example
4850 West Cedar Boulevard
Suite #320
Roswell, GA 30592

Font styles to use
Serif
Sans Serif

Requirements
Must have
• Since 1918
Nice to have
• Could use the 100 Year Logo for back of card, would like the back of card to be the same green as logo.
Should not have
• No black cards please.

```html
<!DOCTYPE html>
<html lang="en">
<head>
<meta charset="utf-8">
<title>K. V. Tillet Business Card</title>
<link href="https://fonts.googleapis.com/css2?family=Roboto:wght@400;500;700;900&display=swap" rel="stylesheet">
<style>
  :root {
    --brand-green: #0e9a5c;
    --paper-white: #ffffff;
    --stage: #e7e9e8;
    --card-shadow: rgba(0, 0, 0, 0.18);
  }
  * { margin: 0; padding: 0; box-sizing: border-box; }
  html, body { width: 1200px; height: 768px; overflow: hidden; }
  body {
    background: var(--stage);
    font-family: "Roboto", Arial, sans-serif;
    display: flex;
    align-items: center;
    justify-content: center;
    gap: 40px;
  }
  .card {
    position: relative;
    width: 540px;
    height: 310px;
    border-radius: 22px;
    overflow: hidden;
    box-shadow: 0 10px 24px var(--card-shadow);
  }
  /* Back side */
  .card-back {
    background: var(--brand-green);
    color: var(--paper-white);
  }
  .back-mark {
    position: absolute;
    top: 78px;
    left: 0;
    right: 0;
    display: flex;
    flex-direction: column;
    align-items: center;
    gap: 12px;
  }
  .mark-dot {
    width: 60px;
    height: 60px;
    border-radius: 50%;
    background: var(--paper-white);
  }
  .back-name {
    font-weight: 700;
    font-size: 26px;
    letter-spacing: 0.5px;
    line-height: 1.1;
  }
  .back-since {
    font-size: 12px;
    letter-spacing: 3px;
    text-transform: uppercase;
    margin-top: -6px;
  }
  .back-url {
    position: absolute;
    bottom: 30px;
    left: 0;
    right: 0;
    text-align: center;
    font-size: 13px;
    letter-spacing: 5px;
  }
  /* Front side */
  .card-front { background: var(--brand-green); }
  .front-panel {
    position: absolute;
    top: 0;
    left: 0;
    width: 330px;
    height: 100%;
    background: var(--paper-white);
    border-radius: 0 26px 26px 0;
  }
  .front-brand {
    position: absolute;
    top: 80px;
    left: 0;
    width: 330px;
    display: flex;
    flex-direction: column;
    align-items: center;
    color: var(--brand-green);
    font-weight: 700;
  }
  .front-brand .mark-dot {
    background: var(--brand-green);
    width: 58px;
    height: 58px;
    margin-bottom: 12px;
  }
  .brand-name { font-size: 27px; line-height: 1.05; }
  .brand-sub { font-size: 11.5px; letter-spacing: 0.4px; margin-top: 3px; }
  .contact {
    position: absolute;
    top: 52px;
    left: 352px;
    right: 12px;
    color: var(--paper-white);
  }
  .person-name { font-weight: 700; font-size: 20px; line-height: 1.1; }
  .person-title { font-size: 12.5px; margin-bottom: 12px; }
  .address { font-size: 11px; line-height: 1.35; margin-bottom: 10px; }
  .contact-list { list-style: none; font-size: 11px; }
  .contact-list li {
    display: flex;
    align-items: center;
    gap: 7px;
    line-height: 1.5;
    white-space: nowrap;
  }
  .contact-list svg { width: 11px; height: 11px; flex: none; fill: var(--paper-white); }
</style>
</head>
<body>
  <section class="card card-back" aria-label="Back of card">
    <div class="back-mark">
      <span class="mark-dot"></span>
      <span class="back-name">K. V. Tillet</span>
      <span class="back-since">Since 1918</span>
    </div>
    <p class="back-url">www.kvtillet.example</p>
  </section>

  <section class="card card-front" aria-label="Front of card">
    <div class="front-panel"></div>
    <div class="front-brand">
      <span class="mark-dot"></span>
      <span class="brand-name">K. V. Tillet</span>
      <span class="brand-sub">Manufacturing Company, Inc.</span>
    </div>
    <div class="contact">
      <p class="person-name">Marco Tillet</p>
      <p class="person-title">Vice President</p>
      <p class="address">4850 West Cedar Boulevard<br>Suite #320<br>Roswell, GA 30592</p>
      <ul class="contact-list">
        <li><svg viewBox="0 0 24 24"><path d="M6.6 10.8a15 15 0 0 0 6.6 6.6l2.2-2.2c.3-.3.7-.4 1-.2 1.1.4 2.3.6 3.6.6.6 0 1 .4 1 1V20c0 .6-.4 1-1 1C10.6 21 3 13.4 3 4c0-.6.4-1 1-1h3.5c.6 0 1 .4 1 1 0 1.3.2 2.5.6 3.6.1.3 0 .7-.2 1z"/></svg>555-284-7130</li>
        <li><svg viewBox="0 0 24 24"><path d="M7 1h10a2 2 0 0 1 2 2v18a2 2 0 0 1-2 2H7a2 2 0 0 1-2-2V3a2 2 0 0 1 2-2zm0 3v14h10V4z"/></svg>555-619-3842</li>
        <li><svg viewBox="0 0 24 24"><path d="M2 5h20v14H2zm2 2v.5l8 5 8-5V7z"/></svg>marco@kvtillet.example</li>
        <li><svg viewBox="0 0 24 24"><circle cx="12" cy="12" r="10"/></svg>www.kvtillet.example</li>
      </ul>
    </div>
  </section>
</body>
</html>
```